WordPress Site Design and Code for Technology Consulting Startup

We need a WordPress design and code to a new site on Nimbo Vault. We have the logo and colors ready. The site will be a brochure site with a CONTACT page that contains a form that the prospective client fills out. The other pages would be ABOUT / SERVICES (3 option drop-down) / SUPPORT. The site should be appropriate for an IT Consulting / IT Managed Services / IT Project Management services in the Chicago area.

Target Market(s)

Across small, medium, large businesses.

Industry/Entity Type

Technology, network infrastructure, IT.

Coding

Coded - Design and coding required

Number of Pages Required

5+ page

Requirements
Nice to have
• I prefer mid-modern / simple / art deco / minimalist.

```html
<!DOCTYPE html>
<html lang="en">
<head>
<meta charset="utf-8">
<title>Corvane — IT Consulting</title>
<link href="https://fonts.googleapis.com/css2?family=Poppins:wght@400;500;600;700;800&display=swap" rel="stylesheet">
<style>
:root{
  --orange:#f6780b;
  --teal:#0c97ab;
  --navy:#0a2443;
  --navy-deep:#061a33;
  --ink:#111;
  --text:#333;
  --muted:#777;
  --paper:#efefef;
  --white:#fff;
  --footer:#171717;
  --play:#e81010;
}
*{box-sizing:border-box;margin:0;padding:0}
html,body{width:1200px;height:3661px;overflow:hidden}
body{font-family:'Poppins',sans-serif;color:var(--text);background:var(--white)}
section,header,footer{position:relative;width:1200px;overflow:hidden}
.abs{position:absolute}
a{color:inherit;text-decoration:none}

/* hero */
.hero{height:627px;background:radial-gradient(ellipse at 78% 35%,#13558a 0%,#0c3565 35%,var(--navy) 65%,var(--navy-deep) 100%)}
.nav{position:absolute;left:0;top:0;width:1200px;height:75px;border-bottom:1px solid rgba(120,170,220,.35)}
.burger{left:84px;top:26px;width:28px}
.burger span{display:block;height:2px;background:var(--white);margin-bottom:7px}
.brand{font-weight:700;letter-spacing:1px;color:var(--teal);font-size:18px}
.nav-links{top:28px;font-size:12px;color:var(--white);font-weight:500}
.nav-links a{position:absolute;white-space:nowrap}
.nav-links .active{color:var(--orange)}
.hero-art{left:700px;top:75px;width:500px;height:552px;background:radial-gradient(circle at 50% 50%,rgba(40,200,240,.45) 0%,rgba(20,110,180,.2) 35%,rgba(10,40,80,0) 65%)}
.eyebrow-hero{left:135px;top:163px;font-size:12px;font-weight:500;color:var(--white)}
.hero h1{left:135px;top:198px;font-size:47px;font-weight:800;line-height:56px}
.hero h1 .o{color:var(--orange);display:block}
.hero h1 .t{color:var(--teal);display:block}
.hero-copy{left:135px;top:320px;width:345px;font-size:13px;line-height:21px;color:var(--white)}
.learn{left:135px;top:450px;font-size:12px;font-weight:600;color:var(--orange);display:flex;align-items:center;gap:12px}
.tabs{top:543px;font-size:12.5px;color:#c8d6e6}
.tabs span{position:absolute;white-space:nowrap}
.tabs .on{color:var(--white);border-top:2px solid var(--orange);padding-top:6px;top:-8px}

/* about */
.about{height:418px;background:var(--paper)}
.about-photo{left:122px;top:40px;width:406px;height:334px;background:linear-gradient(135deg,#d9d6d0,#b9b3aa 50%,#6b6662)}
.eyebrow{font-size:11px;font-weight:600;color:var(--orange);letter-spacing:.3px}
.about .eyebrow{left:610px;top:60px}
.about h2{left:610px;top:81px;font-size:32px;line-height:44px;font-weight:700;color:var(--ink)}
.about p{left:610px;top:183px;width:400px;font-size:12.5px;line-height:20.5px}
.know{left:610px;top:326px;font-size:12px;font-weight:600;color:var(--teal);display:flex;align-items:center;gap:12px}

/* services */
.services{height:455px;background:var(--white);text-align:center}
.services .eyebrow{width:1200px;top:34px;color:var(--teal)}
.services h2{width:1200px;top:56px;font-size:35px;font-weight:700;color:var(--orange)}
.services p{left:275px;top:106px;width:650px;font-size:12.5px;line-height:20.5px}
.svc{top:214px;width:300px;text-align:center}
.svc .disc{width:156px;height:156px;border-radius:50%;background:var(--teal);margin:0 auto;display:flex;align-items:center;justify-content:center}
.svc h3{margin-top:22px;font-size:22px;font-weight:500;color:var(--ink)}

/* pricing */
.pricing{height:565px;background:var(--paper);text-align:center}
.pricing .eyebrow{width:1200px;top:34px}
.pricing h2{width:1200px;top:58px;font-size:32px;font-weight:700;color:var(--ink)}
.plan{top:129px;width:229px;height:400px;background:var(--white);text-align:center}
.plan.featured{border:2px solid var(--orange)}
.plan .tag{position:absolute;left:0;top:0;width:100%;height:17px;background:var(--orange);color:var(--white);font-size:8.5px;font-weight:600;line-height:17px}
.plan .ico{position:absolute;left:0;top:36px;width:100%;height:80px}
.plan .name{position:absolute;top:135px;width:100%;font-size:12px;font-weight:500;color:var(--ink)}
.plan .price{position:absolute;top:152px;width:100%;font-size:23px;color:var(--ink)}
.plan .price b{font-weight:400;color:var(--orange)}
.plan ul{position:absolute;left:38px;top:197px;list-style:none;text-align:left}
.plan li{font-size:9.5px;height:24.5px;display:flex;align-items:flex-start;gap:10px}
.plan li::before{content:"";width:11px;height:11px;border-radius:50%;background:var(--orange);flex:none}
.plan .btn{position:absolute;left:45px;top:340px;width:138px;height:31px;line-height:31px;background:var(--orange);color:var(--white);font-size:11.5px;font-weight:600}
.plan.featured .btn{left:43px;top:338px;background:var(--ink)}

/* video */
.video{height:500px;background:linear-gradient(100deg,#2b2f35 0%,#6a5a4e 40%,#8d7a68 60%,#9fa9b8 100%)}
.play{left:560px;top:213px}

/* blogs */
.blogs{height:626px;background:var(--white)}
.blogs h2{width:1200px;top:30px;text-align:center;font-size:31px;font-weight:700;color:var(--ink)}
.rule{top:51px;height:1px;background:#999;width:252px}
.card{top:99px;width:406px}
.card .pic{height:238px}
.card .cat{margin-top:10px;font-size:8.5px;font-weight:600;color:var(--ink)}
.card h3{margin-top:6px;font-size:19px;line-height:21px;font-weight:600;color:var(--ink)}
.card p{margin-top:14px;font-size:12px;line-height:21px;width:360px}
.card .meta{position:absolute;top:412px;left:0;width:100%;font-size:9px;color:var(--muted)}
.card .meta svg{position:absolute;right:0;top:-4px}
.divider{left:599px;top:99px;width:1px;height:432px;background:#bbb}
.see-all{left:509px;top:549px;width:182px;height:43px;border:1.5px solid var(--ink);text-align:center;line-height:40px;font-size:11px;font-weight:600;color:var(--orange)}

/* cta */
.cta{height:190px;background:var(--orange);color:var(--white)}
.cta h2{top:32px;width:600px;text-align:center;font-size:29px;font-weight:700}
.cta .split{left:599px;top:24px;width:1px;height:142px;background:rgba(255,255,255,.7)}
.cta .btn{width:182px;height:43px;border:1.5px solid var(--white);text-align:center;line-height:40px;font-size:11px;font-weight:600}

/* footer */
.footer{height:280px;background:var(--footer);color:var(--white)}
.footer .brand{left:114px;top:40px;font-size:22px;display:flex;align-items:center;gap:10px}
.footer .brand i{display:block;width:22px;height:22px;border:3px solid var(--orange)}
.footer .about-txt{left:114px;top:100px;width:345px;font-size:12px;line-height:20.5px}
.footer h4{font-size:17px;font-weight:600;border-bottom:1.5px solid var(--white);padding-bottom:4px;letter-spacing:.3px}
.flinks{font-size:12px}
.flinks div{position:absolute;left:0;white-space:nowrap}
.contact-row{position:absolute;left:0;display:flex;align-items:flex-start;gap:14px;font-size:12.5px;line-height:18px;white-space:nowrap}
.contact-row .ci{width:22px;height:22px;border-radius:50%;border:1.5px solid var(--white);display:flex;align-items:center;justify-content:center;flex:none}
.news-input{left:867px;top:71px;width:181px;height:36px;background:#444;color:#bbb;font-size:10.5px;line-height:36px;padding-left:12px}
.news-go{left:1048px;top:71px;width:35px;height:36px;background:var(--orange);display:flex;align-items:center;justify-content:center}
.agree{left:867px;top:128px;display:flex;gap:14px;font-size:11.5px;line-height:19px}
.agree i{display:block;width:16px;height:16px;background:var(--white);margin-top:3px;flex:none}
.foot-line{left:114px;top:234px;width:974px;height:1px;background:#444}
.copy{left:114px;top:250px;font-size:11.5px;color:#ccc}
.social{left:932px;top:251px;display:flex;gap:14px}
.social span{display:block;width:14px;height:14px;border-radius:50%;background:var(--white)}
</style>
</head>
<body>

<header class="hero">
  <div class="hero-art abs" role="img" aria-label="Glowing digital light bulb over a circuit board pattern"></div>
  <nav class="nav">
    <div class="burger abs"><span></span><span></span><span></span></div>
    <div class="brand abs" style="left:134px;top:27px">CORVANE</div>
    <div class="nav-links abs" style="left:0;width:1200px">
      <a class="active" style="left:621px">HOME</a>
      <a style="left:690px">ABOUT US</a>
      <a style="left:784px">SERVICES</a>
      <a style="left:874px">CONTACT</a>
      <a style="left:1038px">EXPLORE</a>
      <svg class="abs" style="left:1112px;top:-4px" width="22" height="22" viewBox="0 0 22 22" fill="none" stroke="#fff" stroke-width="2"><circle cx="9" cy="9" r="7"/><path d="M14 14l6 6"/></svg>
    </div>
  </nav>
  <div class="eyebrow-hero abs">Global Industry Forum</div>
  <h1 class="abs"><span class="o">CONNECTING</span><span class="t">THE WORLD</span></h1>
  <p class="hero-copy abs">Lorem ipsum dolor sit amet, consectetur adipiscing elit, sed do eiusmod tempor incididunt ut labore et dolore magna aliqua. Quis ipsum suspendisse ultrices gravida. Risus commodo viverra maecenas accumsan lacus vel facilisis.</p>
  <a class="learn abs">LEARN MORE <svg width="40" height="10" viewBox="0 0 40 10" fill="none" stroke="currentColor" stroke-width="1.5"><path d="M0 5h38M33 1l5 4-5 4"/></svg></a>
  <div class="tabs abs" style="left:0;width:1200px">
    <span style="left:134px">Customer Love</span>
    <span style="left:347px">M &amp; A Report</span>
    <span class="on" style="left:532px">Global Industry Forum</span>
    <span style="left:815px">Factory of the Future</span>
  </div>
</header>

<section class="about">
  <div class="about-photo abs" role="img" aria-label="Three colleagues in discussion at an office table"></div>
  <div class="eyebrow abs">WHO WE ARE</div>
  <h2 class="abs">GET EXPERTY ADVICE &amp;<br>START YOUR BUSINESS</h2>
  <p class="abs">Lorem ipsum dolor sit amet, consectetur adipiscing elit, sed do eiusmod tempor incididunt ut labore et dolore magna aliqua. Quis ipsum suspendisse ultrices gravida. Risus commodo viverra maecenas accumsan lacus vel facilisis. Lorem ipsum dolor sit amet, consectetcommodo viverra maecenas accumsan lacus vel facilisis..</p>
  <a class="know abs">KNOW MORE <svg width="40" height="10" viewBox="0 0 40 10" fill="none" stroke="currentColor" stroke-width="1.5"><path d="M0 5h38M33 1l5 4-5 4"/></svg></a>
</section>

<section class="services">
  <div class="eyebrow abs">OUR SERVICES</div>
  <h2 class="abs">WHAT INDUSTRY WE SERVE</h2>
  <p class="abs">Lorem ipsum dolor sit amet, consectetur adipiscing elit, sed do eiusmod tempor incididunt ut labore et dolore magna aliqua. Quis ipsum suspendisse ultrices gravida. Risus commodo viverra maecenas accumsan lacus vel facilisis.</p>
  <div class="svc abs" style="left:113px">
    <div class="disc"><svg width="90" height="80" viewBox="0 0 90 80" fill="none" stroke="#fff" stroke-width="3"><rect x="4" y="4" width="34" height="72" rx="3"/><path d="M4 22h34M4 40h34M4 58h34"/><rect x="52" y="14" width="34" height="20" rx="2"/><rect x="52" y="48" width="34" height="20" rx="2"/><path d="M38 24h14M38 58h14"/></svg></div>
    <h3>Network infrastructure</h3>
  </div>
  <div class="svc abs" style="left:450px">
    <div class="disc"><svg width="96" height="96" viewBox="0 0 96 96" fill="none" stroke="#fff" stroke-width="3"><circle cx="48" cy="48" r="42"/><circle cx="48" cy="48" r="7" fill="#fff"/><circle cx="24" cy="30" r="6" fill="#fff"/><circle cx="72" cy="30" r="6" fill="#fff"/><circle cx="26" cy="70" r="6" fill="#fff"/><circle cx="70" cy="70" r="6" fill="#fff"/><circle cx="48" cy="12" r="5" fill="#fff"/><path d="M48 48L24 30M48 48L72 30M48 48L26 70M48 48L70 70M48 48V12M24 30L48 12L72 30"/></svg></div>
    <h3>Technology</h3>
  </div>
  <div class="svc abs" style="left:787px">
    <div class="disc"><svg width="96" height="86" viewBox="0 0 96 86" fill="none" stroke="#fff" stroke-width="3"><rect x="14" y="22" width="68" height="44" rx="3"/><path d="M4 72h88v6H4z"/><path d="M38 38l-8 6 8 6M58 38l8 6-8 6M52 34l-8 20"/><circle cx="48" cy="12" r="8"/></svg></div>
    <h3>Information Technology</h3>
  </div>
</section>

<section class="pricing">
  <div class="eyebrow abs">PLANS &amp; PRICING</div>
  <h2 class="abs">Flexible monthly plans</h2>

  <div class="plan abs" style="left:218px">
    <svg class="ico" viewBox="0 0 229 80" fill="none" stroke="#111" stroke-width="3"><circle cx="114.5" cy="22" r="15"/><path d="M84 76c0-20 14-32 30.5-32S145 56 145 76z"/></svg>
    <div class="name">SMALL</div>
    <div class="price"><b>$398</b>/mo</div>
    <ul><li>Lorem ipsum dolor sit amet,</li><li>Lorem ipsum dolor sit amet,</li><li>Lorem ipsum dolor sit amet,</li><li>Lorem ipsum dolor sit amet,</li><li>Lorem ipsum dolor sit amet,</li></ul>
    <a class="btn">SUBSCRIBE NOW</a>
  </div>

  <div class="plan featured abs" style="left:484px;top:127px;width:233px;height:404px">
    <div class="tag">GET SUBSCRIPTION</div>
    <svg class="ico" viewBox="0 0 233 80" fill="none" stroke="#111" stroke-width="3"><circle cx="86" cy="30" r="10"/><circle cx="116.5" cy="22" r="12"/><circle cx="147" cy="30" r="10"/><path d="M70 76V56c0-8 8-12 16-12s14 4 14 12v20M100 76V50c0-8 8-14 16.5-14S133 42 133 50v26M133 76V56c0-8 6-12 14-12s16 4 16 12v20"/></svg>
    <div class="name">MEDIUM</div>
    <div class="price"><b>$698</b>/mo</div>
    <ul style="left:38px"><li>Lorem ipsum dolor sit amet,</li><li>Lorem ipsum dolor sit amet,</li><li>Lorem ipsum dolor sit amet,</li><li>Lorem ipsum dolor sit amet,</li><li>Lorem ipsum dolor sit amet,</li></ul>
    <a class="btn">SUBSCRIBE NOW</a>
  </div>

  <div class="plan abs" style="left:752px">
    <svg class="ico" viewBox="0 0 229 80" fill="none" stroke="#111" stroke-width="2.5"><circle cx="114.5" cy="18" r="9"/><circle cx="96" cy="40" r="9"/><circle cx="133" cy="40" r="9"/><circle cx="114.5" cy="62" r="9"/><path d="M104 18h-12M125 18h12M100 50v8M129 50v8"/></svg>
    <div class="name">LARGE</div>
    <div class="price"><b>$998</b>/mo</div>
    <ul><li>Lorem ipsum dolor sit amet,</li><li>Lorem ipsum dolor sit amet,</li><li>Lorem ipsum dolor sit amet,</li><li>Lorem ipsum dolor sit amet,</li><li>Lorem ipsum dolor sit amet,</li></ul>
    <a class="btn">SUBSCRIBE NOW</a>
  </div>
</section>

<section class="video" role="img" aria-label="Video still of three consultants reviewing plans in a lounge">
  <svg class="play abs" width="84" height="92" viewBox="0 0 84 92"><path d="M0 0L84 46L0 92z" fill="var(--play)"/></svg>
</section>

<section class="blogs">
  <div class="rule abs" style="left:185px"></div>
  <h2 class="abs">Our Blogs &amp; News</h2>
  <div class="rule abs" style="left:763px"></div>

  <article class="card abs" style="left:185px;height:430px">
    <div class="pic" role="img" aria-label="Paved path through a green forest" style="background:linear-gradient(180deg,#4f7a2e,#6f9a45 50%,#8a8a80)"></div>
    <div class="cat">Sustainability &amp; Responsibility</div>
    <h3>Voluntary Carbon Markets in 2023: A Bumpy Road Behind, Crossroads Ahead</h3>
    <p>The markets for carbon credits will either rationalize or be stifled by uncertainty and complexity.</p>
    <div class="meta">Brief <svg width="14" height="18" viewBox="0 0 14 18" fill="none" stroke="#333" stroke-width="1.5"><path d="M1 1h12v16l-6-5-6 5z"/></svg></div>
  </article>
  <div class="divider abs"></div>
  <article class="card abs" style="left:609px;height:430px">
    <div class="pic" role="img" aria-label="Engineer inspecting metal parts in a factory" style="background:linear-gradient(135deg,#c9c4bb,#8e8a86 55%,#5b5a5c)"></div>
    <div class="cat">Procurement</div>
    <h3>Circular Transformation of Industries: Unlocking New Value in a Resource-Constrained World</h3>
    <p>Circularity initiatives to date have shown that isolated efforts are not enough.</p>
    <div class="meta">Global Industry Forum <svg width="14" height="18" viewBox="0 0 14 18" fill="none" stroke="#333" stroke-width="1.5"><path d="M1 1h12v16l-6-5-6 5z"/></svg></div>
  </article>
  <a class="see-all abs">SEE ALL BLOGS</a>
</section>

<section class="cta">
  <h2 class="abs" style="left:0">What can we help you achieve?</h2>
  <div class="split abs"></div>
  <h2 class="abs" style="left:565px">Where will your career take you?</h2>
  <a class="btn abs" style="left:246px;top:103px">LET'S GET TO WORK</a>
  <a class="btn abs" style="left:773px;top:95px">COME FIND OUT</a>
</section>

<footer class="footer">
  <div class="brand abs"><i></i>CORVANE</div>
  <p class="about-txt abs">Lorem ipsum dolor sit amet, consectetur adipiscing elit, sed do eiusmod tempor incididunt ut labore et dolore magna aliqua. Quis ipsum suspendisse ultrices gravida. Risus commodo viverra maecenas</p>

  <div class="abs" style="left:465px;top:36px"><h4>USEFUL LINKS</h4></div>
  <div class="flinks abs" style="left:466px;top:84px">
    <div style="top:0">HOME</div><div style="top:41px">ABOUT US</div><div style="top:81px">SERVICES</div><div style="top:121px">CONTACT</div>
  </div>

  <div class="abs" style="left:634px;top:36px"><h4>CONTACT US</h4></div>
  <div class="abs" style="left:634px;top:80px">
    <div class="contact-row" style="top:0"><span class="ci"><svg width="11" height="11" viewBox="0 0 12 12" fill="#fff"><path d="M2 1l2.5 0 1 3-1.5 1c.6 1.4 1.6 2.4 3 3l1-1.5 3 1V10c0 .6-.5 1-1 1C5 11 1 7 1 2c0-.5.4-1 1-1z"/></svg></span>1005550142</div>
    <div class="contact-row" style="top:44px"><span class="ci"><svg width="11" height="9" viewBox="0 0 12 9" fill="none" stroke="#fff" stroke-width="1.3"><rect x=".7" y=".7" width="10.6" height="7.6"/><path d="M1 1l5 4 5-4"/></svg></span>hello@corvane-mail.test</div>
    <div class="contact-row" style="top:89px"><span class="ci"><svg width="11" height="11" viewBox="0 0 12 12" fill="none" stroke="#fff" stroke-width="1.2"><circle cx="6" cy="6" r="5"/><path d="M1 6h10M6 1c2 2 2 8 0 10M6 1c-2 2-2 8 0 10"/></svg></span>www.corvane<br>itsolution.test</div>
  </div>

  <div class="abs" style="left:866px;top:36px"><h4>OUR NEWSLETTER</h4></div>
  <div class="news-input abs">ENTER YOUR EMAIL</div>
  <div class="news-go abs"><svg width="12" height="18" viewBox="0 0 12 18" fill="none" stroke="#fff" stroke-width="2.5"><path d="M2 2l7 7-7 7"/></svg></div>
  <div class="agree abs"><i></i><span>*I have read the Privacy Policy<br>and agree to its terms.</span></div>

  <div class="foot-line abs"></div>
  <div class="copy abs">© 2023 CORVANE. All Rights Reserved.</div>
  <div class="social abs" aria-label="Social links"><span></span><span></span><span></span><span></span><span></span></div>
</footer>

</body>
</html>
```